Mini Book (4.25 x 6) Cover Design for Christian authors

We need a book cover designed for a mini book (4.25 x 6). We will need a front, back and spine for the book.
The book is titled:
Harbor Lanterns
Subtitle:
Quiet Meaning Held in Your Name
Authors:
Walter and Renata Oskarsby
We are wanting the colors Dark Blue and Grey with more blue than grey.
We do not want any stock images or photos, only original work.
The cover should convey sincerity, intuition and truth with prestige.
We want the back cover text to be included (top) and the bios to be on the back as well (bottom). *Those documents are included in the files.
Since it is a mini book, it is important for the design to be simple and not cluttered, but powerful!
This is the first book in a twelve book series, so we would like the same "look" to carry through all twelve books, eventually.
On the back of the book, at the bottom (left), we want the following contact information:
Bright Meadow Method Logo (in files below)
tallwillowstudio@mailfernly.com
303.512.4086
P.O.Box 718
Sedalia, CO 80417

Please save room on the back (bottom-right) for the ISBN and price.
Updates

Thank you to the designers that have submitted feedback concerning our design brief. We have made some changes that will perhaps make it easier to submit a variety of designs.Thank you! Added Saturday, March 4, 2017

Target Market(s)

Christians - mainly women

Industry/Entity Type

Religious

Font styles to use
Serif
Sans Serif
Decorative
Script
Other font styles liked:
• Not any particular font, looking for one that goes well with the cover design.

Requirements
Must have
• Mini Book Size (4.25 x 6)-spine size 1/8" (0.125)
• Dark blue and grey colors
• Cover needs to be simple and not cluttered or busy.
• Intriguing
• A font that is attractive, but it is still easy to read.
• *File information below
Nice to have
• Designs that are different from the mainstream.
• Perhaps a design that would do something different with the title/font? Maybe a repeat of the words from smaller to larger? Not sure how it would look, but maybe?
Should not have
• Any other colors but dark blue and grey
• Cluttered Look

```html
<!DOCTYPE html>
<html lang="en">
<head>
<meta charset="utf-8">
<title>Harbor Lanterns — Book Cover</title>
<link href="https://fonts.googleapis.com/css2?family=Fira+Sans:wght@600;700&family=Lato:wght@300;400&family=Norican&display=swap" rel="stylesheet">
<style>
  :root {
    --ink-white: #ffffff;
    --deep-navy: #020616;
    --midnight: #061a5c;
    --royal-blue: #0a3fd6;
    --sky-glow: #bfe8ff;
    --aqua-glow: #5ff0ff;
    --haze-grey: #8d93a6;
  }
  * { margin: 0; padding: 0; box-sizing: border-box; }
  html, body {
    width: 850px;
    height: 1200px;
    overflow: hidden;
    background: var(--deep-navy);
  }
  .cover {
    position: relative;
    width: 850px;
    height: 1200px;
    overflow: hidden;
    background:
      radial-gradient(ellipse 200px 150px at 440px 410px, var(--sky-glow) 0%, rgba(191,232,255,0) 100%),
      radial-gradient(ellipse 160px 110px at 790px 400px, var(--aqua-glow) 0%, rgba(95,240,255,0) 100%),
      radial-gradient(ellipse 300px 240px at 420px 400px, rgba(70,150,255,0.9) 0%, rgba(70,150,255,0) 100%),
      radial-gradient(ellipse 220px 260px at 120px 420px, rgba(31,92,240,0.9) 0%, rgba(31,92,240,0) 100%),
      radial-gradient(ellipse 260px 200px at 700px 160px, rgba(40,110,245,0.8) 0%, rgba(40,110,245,0) 100%),
      radial-gradient(ellipse 160px 130px at 130px 880px, rgba(30,90,220,0.55) 0%, rgba(30,90,220,0) 100%),
      linear-gradient(180deg, var(--haze-grey) 0%, #2b3f9c 9%, var(--royal-blue) 28%, #0a33b8 46%, var(--midnight) 62%, #04103a 78%, var(--deep-navy) 100%);
  }
  .authors {
    position: absolute;
    top: 66px;
    left: 0;
    width: 100%;
    text-align: center;
    font-family: "Fira Sans", sans-serif;
    font-weight: 700;
    color: var(--ink-white);
    text-transform: uppercase;
    font-size: 45px;
    line-height: 54px;
    letter-spacing: 0.5px;
  }
  .authors .joiner {
    font-weight: 600;
    font-size: 31px;
  }
  .book-title { font-weight: 400; }
  .title {
    position: absolute;
    left: 0;
    width: 100%;
    text-align: center;
    font-family: "Norican", cursive;
    font-weight: 400;
    color: var(--ink-white);
    line-height: 1;
    white-space: nowrap;
  }
  .title-main { top: 430px; font-size: 250px; }
  .title-second { top: 690px; font-size: 175px; padding-left: 150px; }
  .subtitle {
    position: absolute;
    top: 936px;
    left: 0;
    width: 100%;
    text-align: center;
    font-family: "Lato", sans-serif;
    font-weight: 400;
    font-size: 47px;
    color: var(--ink-white);
    letter-spacing: 0.3px;
  }
</style>
</head>
<body>
  <main class="cover">
    <p class="authors">
      Walter <span class="joiner">and</span><br>
      Renata Oskarsby
    </p>
    <h1 class="book-title">
      <span class="title title-main">Harbor</span>
      <span class="title title-second">Lanterns</span>
    </h1>
    <p class="subtitle">Quiet Meaning Held in Your Name</p>
  </main>
</body>
</html>
```